PowerPoint Design Project

Lanterfield Estate Partners is a Melbourne based property development management company. We provide a comprehensive range of development management services to a select group of listed developers, private landowners, overseas investors and development partners and institutional clients. Our website provides additional information about the company:
http://www.lanterfieldep.example.au
We are looking for a versatile powerpoint design that can be used across a wide variety of presentations including; pitch documents, client reports, Information memorandums, and downloadable credential packs etc. We have attached a good example document.
Updates

Industry/Entity Type

It Company

Requirements
Must have
• The design should have the following slides as a minimum: Intro Page, transition slides, profile slides, slides for graphics,

```html
<!DOCTYPE html>
<html lang="en">
<head>
<meta charset="utf-8">
<title>Lanterfield Estate Partners — Intro Slide</title>
<link href="https://fonts.googleapis.com/css2?family=Open+Sans:wght@400;600;700&family=Roboto+Condensed:wght@700&display=swap" rel="stylesheet">
<style>
  :root {
    --page-bg: #ffffff;
    --ink-dark: #1c1c1c;
    --ink-mid: #555555;
    --ink-soft: #5f5f5f;
    --rule: #e6e6e6;
    --texture-tone: #e9e9e9;
    --footer-band: #54595b;
    --footer-strip: #c9cacb;
    --footer-text: #ffffff;
  }
  * { box-sizing: border-box; margin: 0; padding: 0; }
  html, body { width: 1200px; height: 900px; overflow: hidden; background: var(--page-bg); }
  .slide {
    position: relative;
    width: 1200px;
    height: 900px;
    overflow: hidden;
    background: var(--page-bg);
    font-family: "Open Sans", Arial, sans-serif;
  }
  .backdrop-texture {
    position: absolute;
    left: 420px;
    top: -60px;
    width: 900px;
    height: 860px;
    background:
      radial-gradient(ellipse 55% 45% at 85% 25%, var(--texture-tone) 0%, rgba(233,233,233,0.6) 40%, rgba(255,255,255,0) 75%),
      radial-gradient(ellipse 45% 30% at 60% 55%, rgba(238,238,238,0.8) 0%, rgba(255,255,255,0) 70%);
  }
  .brand-name {
    position: absolute;
    right: 45px;
    top: 326px;
    font-size: 28px;
    font-weight: 700;
    color: var(--ink-dark);
    letter-spacing: -0.3px;
    white-space: nowrap;
  }
  .header-rule {
    position: absolute;
    left: 470px;
    right: 0;
    top: 383px;
    height: 1px;
    background: linear-gradient(to right, rgba(230,230,230,0), var(--rule) 30%, var(--rule));
  }
  .title-block {
    position: absolute;
    right: 52px;
    top: 414px;
    text-align: right;
  }
  .project-title {
    font-size: 43px;
    font-weight: 400;
    color: var(--ink-mid);
    line-height: 1.2;
    letter-spacing: -0.3px;
  }
  .project-title .lead { color: var(--ink-dark); }
  .project-date {
    margin-top: 14px;
    font-size: 22px;
    font-weight: 600;
    color: var(--ink-mid);
  }
  .project-summary {
    margin-top: 18px;
    font-size: 20px;
    line-height: 33px;
    color: var(--ink-soft);
  }
  .footer-strip {
    position: absolute;
    left: 0; right: 0;
    top: 844px;
    height: 8px;
    background: var(--footer-strip);
  }
  .footer-band {
    position: absolute;
    left: 0; right: 0;
    top: 852px;
    height: 48px;
    background: var(--footer-band);
    display: flex;
    align-items: center;
    justify-content: space-between;
    padding: 0 52px 0 35px;
    font-family: "Roboto Condensed", "Arial Narrow", sans-serif;
    font-weight: 700;
    font-size: 20px;
    color: var(--footer-text);
    letter-spacing: 0.4px;
  }
</style>
</head>
<body>
  <main class="slide">
    <div class="backdrop-texture" role="img" aria-label="Soft grey halftone dot texture fading across the right side"></div>

    <div class="brand-name">Lanterfield Estate Partners</div>
    <div class="header-rule"></div>

    <section class="title-block">
      <h1 class="project-title"><span class="lead">Project</span> Title Here</h1>
      <p class="project-date">Date : 01 - 01 - 2013</p>
      <p class="project-summary">Sub text here Sub text here Sub text here Sub text here<br>Sub text here Sub text here Sub text here Sub</p>
    </section>

    <div class="footer-strip"></div>
    <footer class="footer-band">
      <span class="page-number">Page No. 00</span>
      <span class="copyright">Copyright@2013</span>
    </footer>
  </main>
</body>
</html>
```